Bolts & Burdens: Mending Beyond Engines

AUTHORS BIO:
Derek Moslund is a 20-year Allied Skyward Defense Corps veteran who served as a Crew Chief for K-37 and K-48 fighter jets, maintaining the backbone of America’s air superiority through multiple deployments to Afghanistan and other austere locations. Shaped by the loss of his father as a young adult and the lingering scars of childhood trauma, he confronts PTSD with the same tenacity he brought to the flightline. A survivor and advocate, he brings a raw, hard-earned perspective to "Bolts and Burdens," blending the grit of a serviceman with the insight of a man determined to heal. Focused on helping men confront their pain and find strength in vulnerability. Derek now lives in Jacksonville, North Carolina, where he continues to advocate for those shaped by trauma’s lasting weight.

SUMMARY:
In this raw and revealing non-fiction work, Derek Moslund delves into the lasting echoes of childhood trauma and its profound impact on adult life, with a lens on his 20-year career in the Skyward Defense. Blending personal experience with hard-earned insight, the book explores how post-traumatic stress disorder (PTSD) shapes the mind and body, often in ways that remain hidden until the pressure builds beyond breaking points. With a focus on men—who are too often taught to bury their pain—this narrative offers a roadmap to understanding, confronting, and healing from the torque of trauma. Written in a direct, unflinching voice, "Bolts and Burdens" is both a memoir of resilience and a call to action for those ready to face the past to reclaim their future. Thank you for joining me on this adventure called life. It means more to me than you will ever know.

Target Market(s)

Those serving in the military and post military life with an emphasis on trauma

Font styles to use
Serif

Requirements
Must have
• ASDC K-37 or K-48 aircraft, NO AI GENERATED AIRCRAFT please
Nice to have
• An American Flag
Should not have
• AI generated aircraft

```html
<!DOCTYPE html>
<html lang="en">
<head>
<meta charset="utf-8">
<title>Bolts and Burdens — Book Cover</title>
<link href="https://fonts.googleapis.com/css2?family=Cinzel:wght@400;500;700&display=swap" rel="stylesheet">
<style>
  :root {
    --page: #ffffff;
    --sky-dark: #1f2a30;
    --sky-mid: #56656d;
    --sky-glow: #eadcc8;
    --cloud: #d9dcdf;
    --flag-red: #7a2a1f;
    --title-red: #5a1515;
    --band-red: #4b1414;
    --ink-black: #111111;
    --text-light: #ffffff;
    --jet-light: #9aa3ae;
    --jet-dark: #4d5664;
  }
  * { margin: 0; padding: 0; box-sizing: border-box; }
  html, body { width: 1200px; height: 1200px; overflow: hidden; background: var(--page); }
  .canvas { position: relative; width: 1200px; height: 1200px; }

  .cover {
    position: absolute; left: 242px; top: 63px; width: 716px; height: 1074px;
    overflow: hidden; font-family: "Cinzel", "Times New Roman", serif;
  }
  .cover-art {
    position: absolute; inset: 0 0 99px 0;
    background:
      radial-gradient(ellipse 40% 25% at 35% 50%, rgba(234,220,200,0.9) 0%, rgba(234,220,200,0) 100%),
      linear-gradient(172deg, rgba(122,42,31,0) 18%, rgba(122,42,31,0.6) 23%, rgba(122,42,31,0) 28%, rgba(122,42,31,0.55) 33%, rgba(122,42,31,0) 38%),
      linear-gradient(180deg, var(--sky-dark) 0%, var(--sky-mid) 26%, #b0a596 48%, #8f99a1 72%, var(--cloud) 100%);
  }
  .aircraft {
    position: absolute; left: 65px; top: 344px; width: 566px; height: 286px;
    border-radius: 18px;
    background: linear-gradient(160deg, var(--jet-light) 0%, var(--jet-dark) 100%);
  }

  .subtitle {
    position: absolute; left: 0; right: 0; top: 40px;
    text-align: center; color: var(--text-light);
    font-size: 40px; font-weight: 500; letter-spacing: 1px; line-height: 1;
  }
  .title { position: absolute; inset: 0; color: var(--title-red); font-weight: 400; }
  .title-line, .title-and {
    position: absolute; left: 0; right: 0; text-align: center; display: block;
  }
  .title-line { font-size: 120px; line-height: 120px; font-weight: 500; }
  .title-top { top: 644px; }
  .title-bottom { top: 824px; }
  .title-and {
    top: 770px; color: var(--ink-black); font-size: 54px; line-height: 54px; font-weight: 700;
  }
  .author-band {
    position: absolute; left: 0; right: 0; bottom: 0; height: 99px;
    background: var(--band-red);
    display: flex; align-items: center; justify-content: center;
  }
  .author-name { color: var(--text-light); font-size: 48px; font-weight: 400; letter-spacing: 1px; line-height: 1; }
</style>
</head>
<body>
<div class="canvas">
  <div class="cover">
    <div class="cover-art" role="img" aria-label="Weathered American flag waving across a dramatic cloudy sky with warm light breaking through"></div>
    <div class="aircraft" role="img" aria-label="Photograph of a grey stealth fighter jet banking through the clouds"></div>
    <p class="subtitle">MENDING BEYOND ENGINES</p>
    <h1 class="title">
      <span class="title-line title-top">BOLTS</span>
      <span class="title-and">AND</span>
      <span class="title-line title-bottom">BURDENS</span>
    </h1>
    <div class="author-band"><span class="author-name">AUTHOR NAME</span></div>
  </div>
</div>
</body>
</html>
```